Oven Cleaning flyer design

Hi there,
I need help designing a letterbox flyer. It needs to be DL size.
I have attached a rough design made with Chat GPT.
Would like back and front, have my business colors.
Please find attached mock up of what I would roughly like.
Also find attached logo.
Thank you

Target Market(s)

Home owners over 40

Industry/Entity Type

Cleaning

Requirements
Must have
• Logo, before after of oven, brand colors

```html
<!DOCTYPE html>
<html lang="en">
<head>
<meta charset="utf-8">
<title>Bright Oven Care – DL Flyer Front and Back</title>
<link href="https://fonts.googleapis.com/css2?family=Poppins:wght@400;600;700;800&family=Oswald:wght@500;600&family=Montserrat:wght@800;900&display=swap" rel="stylesheet">
<style>
:root{
  --bg:#5f5f5f;
  --paper:#ffffff;
  --ink:#111111;
  --teal:#2ed3e0;
  --teal-mid:#1fb8c4;
  --teal-deep:#0f6f74;
  --red:#c8141c;
  --gold:#e2b866;
}
*{box-sizing:border-box;margin:0;padding:0}
html,body{width:1197px;height:1200px;overflow:hidden;background:var(--bg)}
body{position:relative;font-family:"Poppins",sans-serif;color:var(--ink)}
.flyer{position:absolute;top:100px;width:472px;height:1001px;background:var(--paper);overflow:hidden}
.flyer--front{left:83px}
.flyer--back{left:643px}
.abs{position:absolute}

/* brand */
.brand{position:absolute;display:flex;align-items:center;gap:14px}
.brand__dot{width:62px;height:62px;border-radius:50%;background:var(--teal-mid);flex:none}
.brand__name{font-family:"Poppins",sans-serif;font-weight:800;color:var(--teal-mid);line-height:1.02;letter-spacing:1px}

/* front */
.kitchen-fade{left:0;top:250px;width:472px;height:390px;background:linear-gradient(180deg,#ffffff 0%,#eef0f1 50%,#f5f6f7 100%)}
.pill-heading{left:66px;top:192px;width:339px;height:49px;border-radius:25px;background:var(--ink);color:#fff;font-family:"Montserrat",sans-serif;font-weight:900;font-size:33px;text-align:center;line-height:49px;letter-spacing:1px}
.hero-word{left:0;width:472px;top:238px;text-align:center;font-family:"Montserrat",sans-serif;font-weight:900;font-size:108px;line-height:1;letter-spacing:-1px;background:linear-gradient(180deg,#3fe3ef 0%,#17b3c0 100%);-webkit-background-clip:text;background-clip:text;color:transparent}
.hero-sub{left:0;width:472px;top:334px;text-align:center;font-family:"Montserrat",sans-serif;font-weight:900;font-size:45px;line-height:1}
.intro{left:46px;width:380px;top:395px;text-align:center;font-size:17px;line-height:22px;color:#222}
.intro b{font-weight:700}
.photo{border-radius:20px;border:3px solid #fff;box-shadow:0 0 0 1px #ddd}
.photo--before{left:42px;top:514px;width:186px;height:235px;background:linear-gradient(180deg,#9a9a9a 0%,#3a3a3a 55%,#6b5a45 100%)}
.photo--after{left:243px;top:514px;width:187px;height:235px;background:linear-gradient(180deg,#a8a8a8 0%,#2e2e2e 55%,#4a4a4a 100%)}
.tag{top:750px;height:38px;width:139px;border-radius:19px;background:var(--teal-deep);color:#fff;font-family:"Oswald",sans-serif;font-weight:600;font-size:29px;line-height:38px;text-align:center}
.tag--before{left:66px}
.tag--after{left:270px}
.call-line{left:0;width:472px;top:793px;display:flex;align-items:center;justify-content:center;gap:10px;font-family:"Oswald",sans-serif;font-weight:500;font-size:25px;color:var(--teal)}
.call-line::before,.call-line::after,.also::before,.also::after{content:"";display:block;width:66px;height:1.5px;background:var(--teal)}
.call-sub{left:0;width:472px;top:826px;text-align:center;color:#fff;font-size:26px;font-weight:600}
.phone{height:45px;width:386px;border-radius:23px;background:var(--teal);display:flex;align-items:center;gap:14px;padding-left:10px}
.phone__icon{width:30px;height:30px;border-radius:50%;background:#fff;display:flex;align-items:center;justify-content:center;flex:none}
.phone__num{font-family:"Montserrat",sans-serif;font-weight:900;font-size:35px;color:var(--teal-deep);letter-spacing:2px}
.web{left:0;width:472px;text-align:center;font-size:23px;color:var(--ink)}
.web span{color:var(--teal-mid);font-weight:600}

/* back */
.tech-photo{left:268px;top:0;width:204px;height:680px;background:linear-gradient(160deg,#6a6a6a 0%,#2c2c2c 45%,#1f2a4a 80%);clip-path:polygon(40% 0,100% 0,100% 100%,0 100%,0 48%,22% 34%,12% 30%,30% 18%)}
.why{left:45px;top:148px;font-family:"Oswald",sans-serif;font-weight:500;font-size:27px;line-height:31px}
.why__accent{color:var(--teal-mid)}
.about{left:45px;top:220px;width:215px;font-size:16.5px;line-height:18.8px;color:#222}
.ribbon{left:82px;top:600px;width:74px;height:92px;background:var(--red);clip-path:polygon(0 0,100% 0,100% 100%,50% 80%,0 100%)}
.badge{left:43px;top:463px;width:152px;height:152px;border-radius:50%;background:var(--gold);display:flex;align-items:center;justify-content:center}
.badge__inner{width:130px;height:130px;border-radius:50%;background:var(--red);color:#fff;text-align:center;font-weight:800;display:flex;flex-direction:column;align-items:center;justify-content:center;line-height:1.05}
.badge__small{font-size:12.5px}
.badge__big{font-size:46px;line-height:1}
.badge__big sup{font-size:22px;vertical-align:top}
.badge__big small{font-size:20px}
.perk{top:710px;width:130px;text-align:center;color:#fff;font-size:15.5px;line-height:18.5px}
.perk__icon{width:46px;height:46px;margin:0 auto 8px;border-radius:50%;background:var(--teal);display:flex;align-items:center;justify-content:center;border:3px solid #fff}
.divider{top:718px;width:1px;height:72px;background:#777}
.also{left:0;width:472px;top:810px;display:flex;align-items:center;justify-content:center;gap:4px;color:var(--teal);font-size:18px;font-weight:600}
.also::before,.also::after{width:70px}
.services{left:42px;top:842px;display:flex;align-items:center;gap:12px;color:#fff;font-size:19px}
.services li{list-style:none;display:flex;align-items:center;gap:7px}
.services .sep{color:#888}
</style>
</head>
<body>

<!-- FRONT -->
<section class="flyer flyer--front">
  <div class="abs kitchen-fade" role="img" aria-label="Faded white kitchen background"></div>
  <div class="brand" style="left:60px;top:60px">
    <span class="brand__dot"></span>
    <span class="brand__name" style="font-size:30px">BRIGHT OVEN<br>CARE</span>
  </div>
  <div class="abs pill-heading">BRING YOUR</div>
  <div class="abs hero-word">OVEN</div>
  <div class="abs hero-sub">BACK TO LIFE</div>
  <p class="abs intro">Professional, <b>non-caustic oven cleaning</b> that removes built-up grease, smoke, and burnt grime-leaving your oven looking fresh again</p>

  <svg class="abs" style="left:0;top:600px" width="472" height="290" viewBox="0 0 472 290" aria-hidden="true">
    <path d="M0 60 C120 20 300 120 472 0 V40 C300 150 120 60 0 100 Z" fill="var(--teal)"/>
    <path d="M0 100 C120 60 300 150 472 40 V289 H0 Z" fill="var(--ink)"/>
  </svg>

  <div class="abs photo photo--before" role="img" aria-label="Dirty oven interior before cleaning"></div>
  <div class="abs photo photo--after" role="img" aria-label="Clean oven interior after cleaning"></div>
  <div class="abs tag tag--before">BEFORE</div>
  <div class="abs tag tag--after">AFTER</div>

  <div class="abs call-line">Call Now for</div>
  <div class="abs call-sub">Fast, Professional Service</div>
  <div class="abs phone" style="left:43px;top:869px">
    <span class="phone__icon"><svg width="18" height="18" viewBox="0 0 24 24"><path d="M6.6 10.8a15 15 0 0 0 6.6 6.6l2.2-2.2a1 1 0 0 1 1-.25 11.4 11.4 0 0 0 3.6.6 1 1 0 0 1 1 1V20a1 1 0 0 1-1 1A17 17 0 0 1 3 4a1 1 0 0 1 1-1h3.5a1 1 0 0 1 1 1c0 1.25.2 2.45.6 3.6a1 1 0 0 1-.25 1z" fill="var(--teal-mid)"/></svg></span>
    <span class="phone__num">0400 123 456</span>
  </div>
  <p class="abs web" style="top:929px">www.<span>brightovencare</span>.com.au</p>
</section>

<!-- BACK -->
<section class="flyer flyer--back">
  <div class="abs tech-photo" role="img" aria-label="Technician in navy uniform giving a thumbs up beside an open oven"></div>
  <div class="brand" style="left:43px;top:48px">
    <span class="brand__dot"></span>
    <span class="brand__name" style="font-size:27px">BRIGHT OVEN<br>CARE</span>
  </div>
  <h2 class="abs why"><span class="why__accent">Why Choose</span><br>Bright Oven Care?</h2>
  <p class="abs about">We're a local family business providing professional, non-caustic oven cleaning across Sunshine Coast. Using specialized-equipment and proven cleaning methods, we remove heavy grease, carbon build-up, smoke residue, restoring your oven safely and effectively.</p>

  <svg class="abs" style="left:0;top:580px" width="472" height="317" viewBox="0 0 472 317" aria-hidden="true">
    <path d="M0 80 C80 30 160 90 260 100 C360 110 430 70 472 0 V45 C430 110 360 150 260 140 C160 130 80 90 0 125 Z" fill="var(--teal)"/>
    <path d="M0 125 C80 90 160 130 260 140 C360 150 430 110 472 45 V316 H0 Z" fill="var(--ink)"/>
  </svg>

  <div class="abs ribbon"></div>
  <div class="abs badge">
    <div class="badge__inner">
      <span class="badge__small">MENTION<br>THIS FLYER FOR</span>
      <span class="badge__big"><sup>$</sup>10<small>OFF</small></span>
      <span class="badge__small" style="font-size:15px">YOUR FIRST<br>CLEAN</span>
    </div>
  </div>

  <div class="abs perk" style="left:36px">
    <div class="perk__icon"><svg width="22" height="22" viewBox="0 0 24 24"><circle cx="12" cy="12" r="8" fill="none" stroke="#fff" stroke-width="2.5"/><path d="M8 12l3 3 5-6" stroke="#fff" stroke-width="2.5" fill="none"/></svg></div>
    Reliable<br>Service
  </div>
  <div class="abs divider" style="left:160px"></div>
  <div class="abs perk" style="left:170px">
    <div class="perk__icon"><svg width="22" height="22" viewBox="0 0 24 24"><circle cx="9" cy="13" r="5" fill="#fff"/><circle cx="16" cy="8" r="3" fill="#fff"/><circle cx="17" cy="16" r="2" fill="#fff"/></svg></div>
    Non-Caustic<br>Cleaning
  </div>
  <div class="abs divider" style="left:311px"></div>
  <div class="abs perk" style="left:319px">
    <div class="perk__icon"><svg width="22" height="22" viewBox="0 0 24 24"><path d="M12 3l2.6 5.3 5.8.8-4.2 4.1 1 5.8L12 16.3 6.8 19l1-5.8L3.6 9.1l5.8-.8z" fill="#fff"/></svg></div>
    Satisfaction<br>Guaranteed
  </div>

  <div class="abs also">WE ALSO CLEAN</div>
  <ul class="abs services">
    <li><svg width="15" height="15" viewBox="0 0 24 24"><circle cx="12" cy="12" r="11" fill="var(--teal)"/><path d="M7 12l3.5 3.5L17 9" stroke="#111" stroke-width="2.6" fill="none"/></svg>Cooktops</li>
    <li class="sep">|</li>
    <li><svg width="15" height="15" viewBox="0 0 24 24"><circle cx="12" cy="12" r="11" fill="var(--teal)"/><path d="M7 12l3.5 3.5L17 9" stroke="#111" stroke-width="2.6" fill="none"/></svg>Rangehoods</li>
    <li class="sep">|</li>
    <li><svg width="15" height="15" viewBox="0 0 24 24"><circle cx="12" cy="12" r="11" fill="var(--teal)"/><path d="M7 12l3.5 3.5L17 9" stroke="#111" stroke-width="2.6" fill="none"/></svg>BBQs</li>
  </ul>

  <div class="abs phone" style="left:43px;top:877px">
    <span class="phone__icon"><svg width="18" height="18" viewBox="0 0 24 24"><path d="M6.6 10.8a15 15 0 0 0 6.6 6.6l2.2-2.2a1 1 0 0 1 1-.25 11.4 11.4 0 0 0 3.6.6 1 1 0 0 1 1 1V20a1 1 0 0 1-1 1A17 17 0 0 1 3 4a1 1 0 0 1 1-1h3.5a1 1 0 0 1 1 1c0 1.25.2 2.45.6 3.6a1 1 0 0 1-.25 1z" fill="var(--teal-mid)"/></svg></span>
    <span class="phone__num">0400 123 456</span>
  </div>
  <p class="abs web" style="top:930px">www.<span>brightovencare</span>.com.au</p>
</section>

</body>
</html>
```